Tavio's Pizzeria Direct Mail Postcard

Looking for a direct mail postcard with a similar design as the one attached, with our logo and store information. This has to meet rlmt direct mail standards and have the postage block printed on the back of cards. I will send over text edits once we get the design we like. The back of the card can have store info and coupons, just have to make sure the coupons on the back dont match the same space as coupons on the front so customers can cut them out. Please use the attached card as a guide. I want to have the same basic design

Industry/Entity Type

Pizza Delivery

Colors

Designer to choose colors to be used in the design.

Requirements
Must have
• RLMT Direct Mail capability
Nice to have
• Great pictures

```html
<!DOCTYPE html>
<html lang="en">
<head>
<meta charset="utf-8">
<title>Tavio's Pizzeria Direct Mail Postcard</title>
<link href="https://fonts.googleapis.com/css2?family=Roboto+Condensed:wght@700&family=Sansita:wght@800&display=swap" rel="stylesheet">
<style>
  :root {
    --backdrop: #bfae9a;
    --card-white: #ffffff;
    --ink-brown: #4a3a30;
    --band-brown: #5b4636;
    --stone-light: #ebe8e4;
    --stone-mid: #a89e94;
    --stone-dark: #7d736a;
    --coupon-fill: #e6e0da;
    --brand-red: #c8161d;
    --line-grey: #3e3e3e;
  }
  * { box-sizing: border-box; margin: 0; padding: 0; }
  html, body { width: 1200px; height: 696px; overflow: hidden; }
  body {
    background: var(--backdrop);
    font-family: "Roboto Condensed", "Arial Narrow", sans-serif;
    position: relative;
  }
  .postcard {
    position: absolute;
    top: 140px;
    width: 540px;
    height: 370px;
    overflow: hidden;
    background: var(--card-white);
    box-shadow: 0 8px 18px rgba(0,0,0,0.28);
  }
  .postcard--back { left: 30px; }
  .postcard--front { left: 630px; }

  /* Back */
  .back-photo {
    position: absolute; left: 0; top: 0; width: 330px; height: 158px;
    background:
      radial-gradient(ellipse 70px 50px at 52% 62%, #d9b48a 0%, rgba(217,180,138,0) 100%),
      radial-gradient(ellipse 60px 45px at 18% 30%, #f0c23a 0%, rgba(240,194,58,0) 100%),
      radial-gradient(ellipse 70px 50px at 78% 30%, #8d2f5d 0%, rgba(141,47,93,0) 100%),
      radial-gradient(ellipse 80px 45px at 30% 85%, #d63a2a 0%, rgba(214,58,42,0) 100%),
      radial-gradient(ellipse 90px 50px at 85% 85%, #c8402e 0%, rgba(200,64,46,0) 100%),
      linear-gradient(180deg, #6b8f3a 0%, #4f7a2e 100%);
  }
  .back-band {
    position: absolute; left: 0; top: 158px; width: 330px; height: 10px;
    background: var(--band-brown);
  }
  .back-stone {
    position: absolute; left: 0; top: 168px; width: 330px; height: 202px;
    background: linear-gradient(180deg, #d3cec8 0%, var(--stone-light) 45%, #f7f6f4 100%);
  }
  .back-coupons {
    position: absolute; left: 10px; top: 162px;
    display: flex; gap: 8px;
  }
  .mail-panel {
    position: absolute; left: 330px; top: 0; width: 210px; height: 370px;
    background: var(--card-white);
  }
  .postage-block {
    position: absolute; right: 24px; top: 22px; width: 96px; height: 70px;
    border: 2px solid var(--ink-brown);
  }
  .address-lines {
    position: absolute; left: 20px; right: 22px; top: 150px;
    list-style: none;
  }
  .address-lines li { height: 36px; border-bottom: 1.5px solid var(--line-grey); }

  /* Coupon seal */
  .coupon {
    position: relative;
    color: var(--ink-brown);
    display: flex; flex-direction: column; align-items: center; justify-content: center;
    text-align: center; line-height: 1;
  }
  .coupon svg { position: absolute; inset: 0; width: 100%; height: 100%; }
  .coupon .seal-fill { fill: var(--coupon-fill); }
  .coupon .seal-edge { fill: none; stroke: var(--card-white); stroke-linecap: round; }
  .coupon > :not(svg) { position: relative; }
  .coupon .price { display: flex; align-items: flex-start; }
  .coupon .dollars { font-size: 2.1em; letter-spacing: -0.02em; }
  .coupon .cents { display: flex; flex-direction: column; font-size: 0.8em; text-align: left; padding-top: 0.25em; }
  .coupon .off { font-size: 1em; }
  .coupon .size { font-size: 0.72em; margin-top: 1px; }
  .back-coupons .coupon { width: 72px; height: 72px; font-size: 11px; }
  .front-coupons .coupon { width: 114px; height: 114px; font-size: 16px; }

  /* Front */
  .front-stone {
    position: absolute; inset: 0;
    background:
      radial-gradient(ellipse 160px 90px at 70% 45%, #cfc9c2 0%, rgba(207,201,194,0) 100%),
      linear-gradient(160deg, #b4aaa0 0%, #c9c2ba 40%, var(--stone-mid) 75%, var(--stone-dark) 100%);
  }
  .front-pizza-photo {
    position: absolute; left: -40px; top: 10px; width: 320px; height: 310px;
    border-radius: 50%;
    background:
      radial-gradient(circle at 50% 50%, #e0572f 0%, #cf3f22 50%, #d98b3f 78%, #a7713f 90%, rgba(120,80,50,0) 100%);
  }
  .front-left-photo {
    position: absolute; left: 0; top: 0; width: 70px; height: 370px;
    background: linear-gradient(180deg, #c5342a 0%, #b23a24 60%, #c9402c 100%);
  }
  .front-tomato-photo {
    position: absolute; left: 240px; top: -10px; width: 220px; height: 130px;
    background:
      radial-gradient(ellipse 50px 40px at 62% 50%, #d8271b 0%, rgba(216,39,27,0) 100%),
      radial-gradient(ellipse 40px 30px at 38% 40%, #b57a4e 0%, rgba(181,122,78,0) 100%),
      radial-gradient(ellipse 50px 25px at 75% 15%, #6ea03c 0%, rgba(110,160,60,0) 100%),
      radial-gradient(ellipse 110px 60px at 50% 40%, rgba(230,220,210,0.9) 0%, rgba(230,220,210,0) 100%);
  }
  .front-vegetable-photo {
    position: absolute; left: 0; bottom: 0; width: 260px; height: 80px;
    background:
      radial-gradient(ellipse 60px 40px at 20% 70%, #cf2e22 0%, rgba(207,46,34,0) 100%),
      radial-gradient(ellipse 50px 30px at 75% 70%, #f0d26a 0%, rgba(240,210,106,0) 100%);
  }
  .front-slice-photo {
    position: absolute; right: 0; bottom: 0; width: 195px; height: 160px;
    border-top-left-radius: 80px 60px;
    background:
      radial-gradient(ellipse 70px 50px at 55% 60%, #f1e2b6 0%, rgba(241,226,182,0) 100%),
      radial-gradient(ellipse 60px 40px at 30% 30%, #c4392a 0%, rgba(196,57,42,0) 100%),
      linear-gradient(135deg, #d59a48 0%, #e2b66f 50%, #d4a055 100%);
  }
  .brand-mark {
    position: absolute; right: 14px; top: 62px;
    display: flex; align-items: center; gap: 6px;
    font-family: "Sansita", Georgia, serif; font-weight: 800;
    font-size: 21px; color: var(--brand-red);
  }
  .brand-mark .dot { width: 14px; height: 14px; border-radius: 50%; background: var(--brand-red); }
  .headline {
    position: absolute; left: 285px; top: 172px; width: 250px;
    font-family: "Sansita", Georgia, serif; font-weight: 800;
    color: var(--ink-brown);
    font-size: 40px; line-height: 1.02; text-align: center;
    transform: rotate(-6deg);
    -webkit-text-stroke: 2px #fff;
    paint-order: stroke fill;
    text-shadow: 0 2px 6px rgba(0,0,0,0.35);
  }
  .headline .amount-sign { font-size: 0.65em; }
  .front-coupons {
    position: absolute; left: 44px; top: 238px;
    display: flex; gap: 22px;
  }

  /* Standalone wordmark */
  .wordmark {
    position: absolute; left: 60px; top: 560px;
    display: flex; align-items: center; gap: 10px;
    font-family: "Sansita", Georgia, serif; font-weight: 800;
    font-size: 30px; color: var(--brand-red);
  }
  .wordmark .dot { width: 22px; height: 22px; border-radius: 50%; background: var(--brand-red); }
</style>
</head>
<body>

<section class="postcard postcard--back" aria-label="Postcard back">
  <div class="back-photo" role="img" aria-label="Photo of grilled chicken with peppers, onion and greens"></div>
  <div class="back-band"></div>
  <div class="back-stone" role="img" aria-label="Faded light stone wall texture"></div>
  <div class="back-coupons">
    <div class="coupon"><svg viewBox="0 0 100 100" aria-hidden="true"><circle class="seal-fill" cx="50" cy="50" r="46"/><circle class="seal-edge" cx="50" cy="50" r="46" stroke-width="7" stroke-dasharray="0 9.63"/></svg><div class="price"><span class="dollars">$3</span><span class="cents"><span>00</span><span>any</span></span></div><span class="off">off</span><span class="size">12" or 14"<br>Pizza</span></div>
    <div class="coupon"><svg viewBox="0 0 100 100" aria-hidden="true"><circle class="seal-fill" cx="50" cy="50" r="46"/><circle class="seal-edge" cx="50" cy="50" r="46" stroke-width="7" stroke-dasharray="0 9.63"/></svg><div class="price"><span class="dollars">$3</span><span class="cents"><span>00</span><span>any</span></span></div><span class="off">off</span><span class="size">12" or 14"<br>Pizza</span></div>
    <div class="coupon"><svg viewBox="0 0 100 100" aria-hidden="true"><circle class="seal-fill" cx="50" cy="50" r="46"/><circle class="seal-edge" cx="50" cy="50" r="46" stroke-width="7" stroke-dasharray="0 9.63"/></svg><div class="price"><span class="dollars">$3</span><span class="cents"><span>00</span><span>any</span></span></div><span class="off">off</span><span class="size">12" or 14"<br>Pizza</span></div>
    <div class="coupon"><svg viewBox="0 0 100 100" aria-hidden="true"><circle class="seal-fill" cx="50" cy="50" r="46"/><circle class="seal-edge" cx="50" cy="50" r="46" stroke-width="7" stroke-dasharray="0 9.63"/></svg><div class="price"><span class="dollars">$3</span><span class="cents"><span>00</span><span>any</span></span></div><span class="off">off</span><span class="size">12" or 14"<br>Pizza</span></div>
  </div>
  <div class="mail-panel">
    <div class="postage-block"></div>
    <ul class="address-lines"><li></li><li></li><li></li><li></li></ul>
  </div>
</section>

<section class="postcard postcard--front" aria-label="Postcard front">
  <div class="front-stone" role="img" aria-label="Grey stone brick wall texture"></div>
  <div class="front-left-photo" role="img" aria-label="Photo of a second pizza edge and chili peppers"></div>
  <div class="front-pizza-photo" role="img" aria-label="Photo of a salami, tomato and olive pizza on a wooden board"></div>
  <div class="front-tomato-photo" role="img" aria-label="Photo of cherry tomatoes, peppercorns, sausages and lettuce"></div>
  <div class="front-vegetable-photo" role="img" aria-label="Photo of tomatoes and cheese cubes"></div>
  <div class="front-slice-photo" role="img" aria-label="Photo of a pepperoni and olive pizza slice with stretching cheese"></div>
  <div class="brand-mark"><span class="dot"></span>Tavio's Pizzeria</div>
  <h1 class="headline">14" Party<br>Pizza <span class="amount-sign">$</span>10.00</h1>
  <div class="front-coupons">
    <div class="coupon"><svg viewBox="0 0 100 100" aria-hidden="true"><circle class="seal-fill" cx="50" cy="50" r="46"/><circle class="seal-edge" cx="50" cy="50" r="46" stroke-width="6" stroke-dasharray="0 9.63"/></svg><div class="price"><span class="dollars">$3</span><span class="cents"><span>00</span><span>any</span></span></div><span class="off">off</span><span class="size">12" or 14"<br>Pizza</span></div>
    <div class="coupon"><svg viewBox="0 0 100 100" aria-hidden="true"><circle class="seal-fill" cx="50" cy="50" r="46"/><circle class="seal-edge" cx="50" cy="50" r="46" stroke-width="6" stroke-dasharray="0 9.63"/></svg><div class="price"><span class="dollars">$3</span><span class="cents"><span>00</span><span>any</span></span></div><span class="off">off</span><span class="size">12" or 14"<br>Pizza</span></div>
  </div>
</section>

<div class="wordmark"><span class="dot"></span>Tavio's Pizzeria</div>

</body>
</html>
```